Yacht, Boats, Watersports company needs a redesign of business card

Hello Designers!
We are a Boat dealership company that sells fun in the water, we sell boats, Yachts, Kayaks and also yacht WaterSport toys. We are looking to redesign our business cards in to something a little bit more sophisticated. in a way that we can make better use of our company colors. I'm attaching a zipped file containing the company 3 sets of company logo which one is an horizontal another one is a vertical and also a chromed 3d logo. Also is included two set of business cards that we use and also some designs that i think it's interesting. We use PMS 2026c Orange and PMS 7687C Blue. I would like to see at least two different options with the orange as accent and also using blue as an accent color. It's really important for the business cards to have a font option and size that is legible to most people. Our current website is wwww.corvellamarine.com. Please visit if you want to have a better feeling of the Boat dealership
You can send Single sided or double side options. We are now using single sided but we may be open for a double side option if we really like the design.
Target Market(s)
Marine, boat sales, yacht sales, water toys sales/
Contact Information for Business Card
Name: Dale Pritchett
Address: 718 West Halden Lane,
Dania Beach, FL 33019
Phone: 954-382-7146
Fax: 954:382-7139
Cell: 954-451-8320
Email: 212@corvellamarine.com
Website: corvellamarine.com
Requirements
Must have
- the current information of the business card provided.
logo
use the PMS Colors
Nice to have
- a touch of elegance and sophistication but simple
Should not have
- should not have any typography that is hard to read, the card should be simple but yet sophisticated.

```html
<!DOCTYPE html>
<html lang="en">
<head>
<meta charset="utf-8">
<title>Corvella Marine – Business Card</title>
<link rel="stylesheet" href="https://fonts.googleapis.com/css2?family=Michroma&family=Poppins:wght@400;500;600&display=swap">
<style>
  :root{
    --blue:#1d4f95;
    --blue-deep:#163f7c;
    --orange:#ef5a24;
    --gold:#e6a21c;
    --white:#ffffff;
    --bg:#e9ebef;
  }
  *{margin:0;padding:0;box-sizing:border-box}
  html,body{width:1200px;height:800px;overflow:hidden;background:var(--bg)}
  .stage{position:relative;width:1200px;height:800px}
  .card{position:absolute;top:245px;width:540px;height:310px;border-radius:18px;overflow:hidden;
        box-shadow:0 10px 30px rgba(20,30,60,.18)}
  .card-front{left:40px;background:var(--white)}
  .card-back{left:620px;background:linear-gradient(135deg,var(--blue-deep),var(--blue) 60%,var(--blue-deep))}
  .card svg.wave{position:absolute;inset:0;width:540px;height:310px}

  .brand-name{position:absolute;left:56px;top:70px;font-family:"Michroma",sans-serif;font-size:24px;
              color:var(--blue);letter-spacing:1px;white-space:nowrap}
  .brand-mark{display:inline-block;width:20px;height:20px;border-radius:50%;background:var(--orange);
              vertical-align:middle;margin-right:12px;position:relative;top:-3px}
  .tagline{position:absolute;left:88px;top:116px;font-family:"Poppins",sans-serif;font-size:14px;color:var(--blue);
           display:flex;align-items:center;gap:9px;white-space:nowrap}
  .tagline .dot{width:7px;height:7px;border-radius:50%;background:var(--orange)}

  .web{position:absolute;font-family:"Michroma",sans-serif;letter-spacing:1px;white-space:nowrap}
  .card-front .web{right:28px;bottom:28px;color:var(--white);font-size:14px}
  .card-back .web{right:26px;bottom:22px;color:var(--blue);font-size:12px}
  .web .accent{color:var(--orange)}

  .back-brand{position:absolute;left:38px;top:62px;width:170px;text-align:center}
  .back-brand .ring{width:116px;height:116px;border-radius:50%;border:9px solid var(--orange);margin:0 auto 14px}
  .back-brand .name{font-family:"Michroma",sans-serif;font-size:13px;color:var(--white);letter-spacing:1px}

  .divider{position:absolute;left:232px;top:46px;width:1px;height:140px;background:rgba(255,255,255,.6)}
  .contact{position:absolute;left:252px;top:34px;font-family:"Poppins",sans-serif;color:var(--white)}
  .contact .person{font-family:"Michroma",sans-serif;font-size:15px;margin-bottom:9px;letter-spacing:.5px;white-space:nowrap}
  .contact .person .last{color:var(--orange)}
  .contact ul{list-style:none}
  .contact li{display:flex;align-items:flex-start;gap:8px;font-size:12px;line-height:1.25;margin-bottom:5px;white-space:nowrap}
  .icon{flex:none;width:15px;height:15px;border-radius:50%;background:var(--orange);display:flex;align-items:center;justify-content:center;margin-top:0}
  .icon svg{width:9px;height:9px}
</style>
</head>
<body>
<div class="stage">

  <section class="card card-front" aria-label="Card front">
    <svg class="wave" viewBox="0 0 540 310" aria-hidden="true">
      <path d="M0,296 C90,246 170,232 280,222 C400,211 480,188 540,138 L540,310 L0,310Z" fill="var(--gold)"/>
      <path d="M0,306 C90,258 172,244 282,234 C402,223 482,202 540,152 L540,310 L0,310Z" fill="var(--orange)"/>
      <path d="M0,318 C92,270 175,256 285,246 C405,235 484,216 540,166 L540,310 L0,310Z" fill="var(--blue)"/>
    </svg>
    <div class="brand-name"><span class="brand-mark"></span>CORVELLA MARINE</div>
    <div class="tagline">Boat sales <span class="dot"></span> Yacht sales <span class="dot"></span> Water toys sales</div>
    <div class="web">CORVELLA<span class="accent">MARINE</span>.COM</div>
  </section>

  <section class="card card-back" aria-label="Card back">
    <svg class="wave" viewBox="0 0 540 310" aria-hidden="true">
      <path d="M150,310 C225,248 320,230 415,210 C485,195 522,172 540,140 L540,310Z" fill="var(--gold)"/>
      <path d="M162,310 C237,252 332,236 428,216 C496,201 526,178 540,150 L540,310Z" fill="var(--orange)"/>
      <path d="M176,310 C251,258 346,242 441,222 C506,207 530,184 540,162 L540,310Z" fill="var(--white)"/>
    </svg>

    <div class="back-brand">
      <div class="ring"></div>
      <div class="name">CORVELLA MARINE</div>
    </div>

    <div class="divider"></div>

    <div class="contact">
      <div class="person">DALE <span class="last">PRITCHETT</span></div>
      <ul>
        <li><span class="icon"><svg viewBox="0 0 10 10"><path d="M2 1 L4 1 L4.6 3 L3.4 3.8 C4 5 5 6 6.2 6.6 L7 5.4 L9 6 L9 8 C5 8.5 1.5 5 2 1Z" fill="#fff"/></svg></span>954-382-7146</li>
        <li><span class="icon"><svg viewBox="0 0 10 10"><rect x="2" y="1" width="6" height="3" fill="#fff"/><rect x="1" y="4.5" width="8" height="4" rx="1" fill="#fff"/></svg></span>954:382-7139</li>
        <li><span class="icon"><svg viewBox="0 0 10 10"><rect x="3" y="1" width="4" height="8" rx="1" fill="none" stroke="#fff" stroke-width="1.2"/></svg></span>954-451-8320</li>
        <li><span class="icon"><svg viewBox="0 0 10 10"><rect x="1" y="2.5" width="8" height="5.5" fill="none" stroke="#fff" stroke-width="1.1"/><path d="M1 2.5 L5 5.5 L9 2.5" fill="none" stroke="#fff" stroke-width="1.1"/></svg></span>212@corvellamarine.com</li>
        <li><span class="icon"><svg viewBox="0 0 10 10"><path d="M5 9 C2 5.5 2 4.5 2 4 A3 3 0 0 1 8 4 C8 4.5 8 5.5 5 9Z" fill="#fff"/></svg></span>718 West Halden Lane,<br>Dania Beach, FL 33019</li>
      </ul>
    </div>

    <div class="web">CORVELLA<span class="accent">MARINE</span>.COM</div>
  </section>

</div>
</body>
</html>
```